Label design for an exciting new Vodka brand

We need a label design for a dynamic new Vodka brand called 'Tall amber fern Vodka'. It is a crisp and versatile liquid with a clean and smooth finish. It should appeal to 21-39 year olds, with a slight female skew. Colours, fonts and styles should be modern and relatively neutral - take inspiration from the brand pictures attached.

Target Market(s)

21-39 year olds, both male and female, but with a slight female skew

```html
<!DOCTYPE html>
<html lang="en">
<head>
<meta charset="utf-8">
<title>Tall amber fern Vodka – Label Design</title>
<link rel="stylesheet" href="https://fonts.googleapis.com/css2?family=Kanit:wght@600&family=Raleway:wght@500;700&display=swap">
<style>
  :root {
    --canvas: #eef1f5;
    --navy: #0f3478;
    --royal: #1a4a9a;
    --ocean: #2468b8;
    --orange: #f2541b;
    --sky: #a7c6ea;
    --paper: #ffffff;
    --ink: #1a1a1a;
    --ink-soft: #555b66;
    --placeholder: #e6ebf2;
  }
  html, body {
    margin: 0;
    width: 1200px;
    height: 880px;
    overflow: hidden;
    background: var(--canvas);
  }
  .canvas {
    position: relative;
    width: 1200px;
    height: 880px;
  }
  .label {
    position: absolute;
    top: 55px;
    width: 440px;
    height: 770px;
    overflow: hidden;
    box-shadow: 0 6px 24px rgba(15, 52, 120, 0.15);
  }
  .label--blue { left: 120px; }
  .label--white { left: 640px; }
  .label__art {
    position: absolute;
    inset: 0;
    width: 440px;
    height: 770px;
  }
  .label__volume {
    position: absolute;
    left: 76px;
    top: 268px;
    font: 700 15px/1 "Raleway", sans-serif;
  }
  .label--blue .label__volume { color: #cfe0f5; }
  .label--white .label__volume { color: var(--ocean); }
  .label__title {
    position: absolute;
    left: 16px;
    top: 330px;
    margin: 0;
    font: 600 84px/0.98 "Kanit", sans-serif;
    color: var(--ink);
    letter-spacing: -1px;
  }
  .label__copy {
    position: absolute;
    left: 262px;
    top: 470px;
    width: 150px;
    margin: 0;
    font: 500 9px/1.45 "Raleway", sans-serif;
    text-align: center;
  }
  .label--blue .label__copy { color: var(--paper); }
  .label--white .label__copy { color: var(--ink-soft); }
  .label__tagline {
    position: absolute;
    right: 14px;
    bottom: 28px;
    margin: 0;
    font: 700 14px/1.35 "Raleway", sans-serif;
    color: var(--paper);
    text-align: right;
  }
</style>
</head>
<body>
<main class="canvas">

  <section class="label label--blue">
    <svg class="label__art" viewBox="0 0 440 770" aria-hidden="false">
      <rect class="band-base" width="440" height="770" fill="var(--royal)"/>
      <path class="band-orange" d="M0,60 C120,20 260,10 440,40 L440,150 C300,140 150,190 0,185 Z" fill="var(--orange)"/>
      <path class="band-ocean" d="M0,185 C150,190 300,140 440,150 L440,250 C300,270 150,290 0,260 Z" fill="var(--ocean)"/>
      <path class="band-deep" d="M0,260 C150,290 300,270 440,250 L440,770 L0,770 Z" fill="var(--navy)"/>
      <path class="band-shore" d="M0,650 C120,600 250,680 440,620 L440,770 L0,770 Z" fill="var(--sky)"/>
      <circle class="emblem-ring" cx="126" cy="136" r="98" fill="none" stroke="var(--paper)" stroke-width="4"/>
      <rect class="emblem-illustration" x="100" y="80" width="52" height="112" rx="6" fill="var(--placeholder)" role="img" aria-label="Illustration of a floating glass bottle"/>
      <rect class="volume-icon" x="40" y="258" width="26" height="32" rx="3" fill="var(--placeholder)" role="img" aria-label="Small drinking glass icon"/>
    </svg>
    <span class="label__volume">500,ml</span>
    <h1 class="label__title">Tall amber<br>fern<br>Vodka</h1>
    <p class="label__copy">Distilled five times from winter wheat and filtered through birch charcoal, this spirit pours bright and clear. Serve it ice cold, mix it with citrus, or share it slowly at sunset with friends.</p>
    <p class="label__tagline">It is a crisp and versatile<br>liquid with a clean and smooth finish</p>
  </section>

  <section class="label label--white">
    <svg class="label__art" viewBox="0 0 440 770" aria-hidden="false">
      <rect class="band-base" width="440" height="770" fill="var(--paper)"/>
      <path class="band-orange" d="M0,60 C120,20 260,10 440,40 L440,150 C300,140 150,190 0,185 Z" fill="var(--orange)"/>
      <path class="band-ocean" d="M0,185 C150,190 300,140 440,150 L440,290 C300,330 150,320 0,300 Z" fill="var(--ocean)"/>
      <path class="band-shore" d="M0,650 C120,600 250,680 440,620 L440,770 L0,770 Z" fill="var(--sky)"/>
      <circle class="emblem-ring" cx="126" cy="136" r="98" fill="none" stroke="var(--paper)" stroke-width="4"/>
      <rect class="emblem-illustration" x="100" y="80" width="52" height="112" rx="6" fill="var(--placeholder)" role="img" aria-label="Illustration of a floating glass bottle"/>
      <rect class="volume-icon" x="40" y="258" width="26" height="32" rx="3" fill="var(--placeholder)" role="img" aria-label="Small drinking glass icon"/>
    </svg>
    <span class="label__volume">500,ml</span>
    <h1 class="label__title">Tall amber<br>fern<br>Vodka</h1>
    <p class="label__copy">Distilled five times from winter wheat and filtered through birch charcoal, this spirit pours bright and clear. Serve it ice cold, mix it with citrus, or share it slowly at sunset with friends.</p>
    <p class="label__tagline">It is a crisp and versatile<br>liquid with a clean and smooth finish</p>
  </section>

</main>
</body>
</html>
```